Boutique custom software development company needs new business card

Our nearly 20 year old custom software development company would like to better include the fact that we are now providing Bitcoin services. These new services are B2B include education (how to acquire and securely hold Bitcoin) and integrating Bitcoin payments into existing ecommerce sites or other existing systems. Please keep the card clean and simple. Attached is our current design and some other files. velquor.example

Target Market(s)

businesses owners interested in long term relationship

Industry/Entity Type

Custom software development and Bitcoin

Contact Information for Business Card

Dale Furness, dale@velquor.example, velquor.example, (555) 274-VELQ

Font styles to use
Other font styles liked:
• monospace

Requirements
Must have
• double-sided
Nice to have
• clean and simple
Should not have
• physical address

```html
<!DOCTYPE html>
<html lang="en">
<head>
<meta charset="utf-8">
<title>Velquor Business Card</title>
<link rel="stylesheet" href="https://fonts.googleapis.com/css2?family=Roboto+Mono:wght@400;500;700&display=swap">
<style>
  :root {
    --page: #ffffff;
    --navy: #131a45;
    --navy-line: #2a3266;
    --orange: #f07c22;
    --brand-blue: #3f73b9;
    --white: #ffffff;
    --mono: "Roboto Mono", monospace;
  }
  * { margin: 0; padding: 0; box-sizing: border-box; }
  html, body {
    width: 1200px; height: 1000px; overflow: hidden;
    background: var(--page);
    font-family: var(--mono);
  }
  .canvas { position: relative; width: 1200px; height: 1000px; }

  .card { position: absolute; }
  .card-front { left: 263px; top: 84px; width: 670px; height: 384px; background: var(--navy); }
  .card-back { left: 262px; top: 531px; width: 675px; height: 384px; background: var(--orange); }

  .frame-line { position: absolute; background: var(--navy-line); }
  .frame-top { left: 125px; top: 101px; width: 163px; height: 1px; }
  .frame-side { left: 288px; top: 101px; width: 1px; height: 182px; }
  .frame-bottom { left: 288px; top: 282px; width: 252px; height: 1px; }

  .brand-block {
    position: absolute; left: 135px; top: 120px; width: 133px; height: 133px;
    background: var(--brand-blue);
    display: flex; align-items: center; justify-content: center;
  }
  .brand-block-name { color: var(--white); font-weight: 700; font-size: 20px; letter-spacing: 0.5px; }

  .contact { position: absolute; left: 311px; top: 125px; color: var(--white); }
  .contact-name { color: var(--orange); font-weight: 500; font-size: 27px; line-height: 1; margin-bottom: 12px; letter-spacing: 0.5px; }
  .contact-row { display: flex; align-items: center; gap: 7px; font-size: 17px; height: 29px; }
  .contact-row svg { width: 16px; height: 16px; flex: none; }
  .contact-web { font-size: 17px; margin-top: 18px; }

  .wordmark {
    position: absolute; left: 0; right: 0; top: 128px; text-align: center;
    color: var(--white); font-weight: 700; font-size: 78px; line-height: 1; letter-spacing: 2px;
  }
  .tagline {
    position: absolute; left: 0; right: 0; top: 218px; text-align: center;
    color: var(--white); font-size: 20px; letter-spacing: 0.4px;
  }
  .service-note {
    position: absolute; left: 0; right: 0; top: 262px; text-align: center;
    color: var(--navy); font-weight: 500; font-size: 15px; letter-spacing: 0.4px;
  }
</style>
</head>
<body>
<main class="canvas">
  <section class="card card-front" aria-label="Card front">
    <div class="frame-line frame-top"></div>
    <div class="frame-line frame-side"></div>
    <div class="frame-line frame-bottom"></div>

    <div class="brand-block"><span class="brand-block-name">VELQUOR</span></div>

    <div class="contact">
      <p class="contact-name">Dale Furness</p>
      <p class="contact-row">
        <svg viewBox="0 0 16 16" fill="none" stroke="#ffffff" stroke-width="1.1" aria-hidden="true">
          <path d="M1.5 6.5 L8 2 L14.5 6.5 V14 H1.5 Z"/>
          <path d="M1.5 6.5 L8 10.5 L14.5 6.5"/>
        </svg>
        dale@velquor.example
      </p>
      <p class="contact-row">
        <svg viewBox="0 0 16 16" fill="none" stroke="#ffffff" stroke-width="1.1" aria-hidden="true">
          <rect x="3.5" y="1" width="9" height="14" rx="1"/>
          <line x1="3.5" y1="3.5" x2="12.5" y2="3.5"/>
          <line x1="3.5" y1="12.5" x2="12.5" y2="12.5"/>
        </svg>
        (555) 274-VELQ
      </p>
      <p class="contact-web">www.velquor.example</p>
    </div>
  </section>

  <section class="card card-back" aria-label="Card back">
    <p class="wordmark">VELQUOR</p>
    <p class="tagline">developer of custom applications</p>
    <p class="service-note">now offering bitcoin education &amp; payment integration</p>
  </section>
</main>
</body>
</html>
```